Tail Wagon Probiotic Chews label design to be used on a jar

I want to design a label for probiotic chews packaging. The jar is black with black lid. Jar and label dims attached. I also have created 2 draft designs. I do not want you to use them as inspiration, but it tells you product name and key features in text form. e.g. blue on gold & black design is there so that when we produce a different chew e.g. for joint support, we can color code it with product name to make them similar, but distinct. The KEY feature is to have it stand out in search results. It needs to POP. It has to be bright, colorful and not the same as everything else. There is more information that goes on the "back" of the label, but for the purpose of this project I only care about the "font". You do not need to design the whole label - I just want to see a mock up of the front - we will fill in the other details later.

Target Market(s)

Dog owners in the USA who are interested in detail, but are drawn by emotion

Industry/Entity Type

Functional dog treats / supplements

Other font styles liked:
• something like https://www.glyphharbor.test/softly-curved.font

Colors
0094D4
00A9DD
6FCCEA
C7EBF8
E9F6FB

Requirements
Must have
• Large title readable on mobile in search results (depending on your choice of style) either "Probiotics & Enzymes for Dogs" or "Sunny Tummy Bites", elements visible in the examples I provided.
Nice to have
• bright, vivid color that will make the package stand out, focus on important features, but also ability to expand to other products by adjusting the color palette for e.g. hip & join supplement
Should not have
• Cannot be too busy, unclear

```html
<!DOCTYPE html>
<html lang="en">
<head>
<meta charset="utf-8">
<title>Tail Wagon – Probiotics &amp; Enzymes Label</title>
<link rel="stylesheet" href="https://fonts.googleapis.com/css2?family=Fredoka:wght@500;600;700&family=Poppins:wght@400;500&display=swap">
<style>
  :root {
    --bg: #e6e6e8;
    --sky: #1fb8ea;
    --lime: #7fd63a;
    --orange: #ef6a21;
    --brand-orange: #f06a1f;
    --white: #ffffff;
    --ink: #1d2a3a;
    --dog-a: #e58a2a;
    --dog-b: #3b7fd8;
    --dog-c: #d94fa0;
    --chew-a: #a65a2c;
    --chew-b: #d08346;
  }
  * { box-sizing: border-box; margin: 0; padding: 0; }
  html, body { width: 1200px; height: 1200px; overflow: hidden; }
  body {
    background: var(--bg);
    position: relative;
    font-family: "Poppins", sans-serif;
  }
  .label {
    position: absolute;
    left: 50px; top: 290px;
    width: 1100px; height: 620px;
    overflow: hidden;
    background: var(--sky);
  }
  .band-green {
    position: absolute; left: 0; top: 34px;
    width: 100%; height: 306px;
    background: var(--lime);
  }
  .band-edge { position: absolute; left: 0; width: 100%; height: 14px; }
  .band-edge.top { top: -13px; }
  .band-edge.bottom { bottom: -13px; }
  .band-orange {
    position: absolute; left: 0; bottom: 0;
    width: 100%; height: 84px;
    background: var(--orange);
    color: var(--white);
    text-align: center;
    padding-left: 380px;
    padding-top: 12px;
  }
  .band-orange .claim {
    font-family: "Fredoka", sans-serif;
    font-weight: 500;
    font-size: 24px;
    line-height: 1.2;
    letter-spacing: 0.5px;
  }
  .band-orange .count {
    font-family: "Fredoka", sans-serif;
    font-weight: 500;
    font-size: 21px;
    line-height: 1.2;
    margin-top: 4px;
  }
  .dog-art {
    position: absolute; left: 0; top: 0;
    width: 380px; height: 620px;
    background: linear-gradient(135deg, var(--dog-a) 0%, var(--dog-c) 40%, var(--dog-b) 75%, var(--dog-a) 100%);
    border-radius: 0 140px 0 0;
  }
  .brand-box {
    position: absolute; left: 625px; top: 0;
    width: 230px; height: 150px;
    background: var(--white);
    border-radius: 0 0 18px 18px;
    display: flex; align-items: center; justify-content: center;
    text-align: center;
  }
  .brand-name {
    font-family: "Fredoka", sans-serif;
    font-weight: 700;
    font-size: 46px;
    line-height: 0.98;
    color: var(--brand-orange);
    text-transform: uppercase;
  }
  .title {
    position: absolute; left: 420px; top: 162px;
    width: 640px;
    text-align: center;
    font-family: "Fredoka", sans-serif;
    font-weight: 700;
    color: var(--white);
    text-transform: uppercase;
    line-height: 0.95;
    text-shadow: 0 4px 0 rgba(0,0,0,0.12);
  }
  .title .line1 { font-size: 84px; display: block; }
  .title .line2 { font-size: 78px; display: block; }
  .for-dogs {
    position: absolute; left: 645px; top: 334px;
    width: 190px; height: 40px;
    background: var(--white);
    border-radius: 20px;
    text-align: center;
    font-family: "Fredoka", sans-serif;
    font-weight: 600;
    font-size: 25px;
    line-height: 40px;
    color: var(--sky);
    text-transform: uppercase;
  }
  .benefits {
    position: absolute; left: 470px; top: 392px;
    width: 520px;
    display: grid;
    grid-template-columns: 1fr 1fr;
    row-gap: 6px;
    list-style: none;
  }
  .benefits li {
    display: flex; align-items: center; gap: 10px;
    font-size: 23px; font-weight: 500; color: var(--ink);
    line-height: 1.2;
  }
  .benefits li.wide { grid-column: 1 / span 2; justify-content: center; }
  .benefits svg { width: 20px; height: 20px; flex: none; }
  .flavor {
    position: absolute; left: 990px; top: 385px;
    width: 100px; text-align: center;
  }
  .chew-art {
    width: 76px; height: 60px; margin: 0 auto 6px;
    background: linear-gradient(135deg, var(--chew-b), var(--chew-a));
    border-radius: 12px;
  }
  .flavor-name {
    font-size: 15px; line-height: 1.15; color: var(--ink);
  }
</style>
</head>
<body>
  <section class="label">
    <div class="band-green">
      <svg class="band-edge top" viewBox="0 0 1100 14" preserveAspectRatio="none">
        <polygon fill="#7fd63a" points="0,14 0,7 10,0 20,7 30,0 40,7 50,0 60,7 70,0 80,7 90,0 100,7 110,0 120,7 130,0 140,7 150,0 160,7 170,0 180,7 190,0 200,7 210,0 220,7 230,0 240,7 250,0 260,7 270,0 280,7 290,0 300,7 310,0 320,7 330,0 340,7 350,0 360,7 370,0 380,7 390,0 400,7 410,0 420,7 430,0 440,7 450,0 460,7 470,0 480,7 490,0 500,7 510,0 520,7 530,0 540,7 550,0 560,7 570,0 580,7 590,0 600,7 610,0 620,7 630,0 640,7 650,0 660,7 670,0 680,7 690,0 700,7 710,0 720,7 730,0 740,7 750,0 760,7 770,0 780,7 790,0 800,7 810,0 820,7 830,0 840,7 850,0 860,7 870,0 880,7 890,0 900,7 910,0 920,7 930,0 940,7 950,0 960,7 970,0 980,7 990,0 1000,7 1010,0 1020,7 1030,0 1040,7 1050,0 1060,7 1070,0 1080,7 1090,0 1100,7 1100,14"/>
      </svg>
      <svg class="band-edge bottom" viewBox="0 0 1100 14" preserveAspectRatio="none">
        <polygon fill="#7fd63a" points="0,0 0,7 10,14 20,7 30,14 40,7 50,14 60,7 70,14 80,7 90,14 100,7 110,14 120,7 130,14 140,7 150,14 160,7 170,14 180,7 190,14 200,7 210,14 220,7 230,14 240,7 250,14 260,7 270,14 280,7 290,14 300,7 310,14 320,7 330,14 340,7 350,14 360,7 370,14 380,7 390,14 400,7 410,14 420,7 430,14 440,7 450,14 460,7 470,14 480,7 490,14 500,7 510,14 520,7 530,14 540,7 550,14 560,7 570,14 580,7 590,14 600,7 610,14 620,7 630,14 640,7 650,14 660,7 670,14 680,7 690,14 700,7 710,14 720,7 730,14 740,7 750,14 760,7 770,14 780,7 790,14 800,7 810,14 820,7 830,14 840,7 850,14 860,7 870,14 880,7 890,14 900,7 910,14 920,7 930,14 940,7 950,14 960,7 970,14 980,7 990,14 1000,7 1010,14 1020,7 1030,14 1040,7 1050,14 1060,7 1070,14 1080,7 1090,14 1100,7 1100,0"/>
      </svg>
    </div>

    <div class="band-orange">
      <p class="claim">DIGESTIVE HEALTH / PROBIOTIC SUPPORT</p>
      <p class="count">170 Chews</p>
    </div>

    <div class="dog-art" role="img" aria-label="Illustration of a smiling dog with rainbow-coloured fur"></div>

    <div class="brand-box">
      <span class="brand-name">Tail<br>Wagon</span>
    </div>

    <h1 class="title">
      <span class="line1">Probiotics</span>
      <span class="line2">&amp; Enzymes</span>
    </h1>

    <div class="for-dogs">For Dogs</div>

    <ul class="benefits">
      <li><svg viewBox="0 0 22 22"><circle cx="11" cy="11" r="9.5" fill="none" stroke="#1d2a3a" stroke-width="1.8"/><polyline points="6.5,11.5 9.7,14.5 15.5,8" fill="none" stroke="#1d2a3a" stroke-width="2" stroke-linecap="round" stroke-linejoin="round"/></svg>No More Gas</li>
      <li><svg viewBox="0 0 22 22"><circle cx="11" cy="11" r="9.5" fill="none" stroke="#1d2a3a" stroke-width="1.8"/><polyline points="6.5,11.5 9.7,14.5 15.5,8" fill="none" stroke="#1d2a3a" stroke-width="2" stroke-linecap="round" stroke-linejoin="round"/></svg>Loved By Dogs</li>
      <li><svg viewBox="0 0 22 22"><circle cx="11" cy="11" r="9.5" fill="none" stroke="#1d2a3a" stroke-width="1.8"/><polyline points="6.5,11.5 9.7,14.5 15.5,8" fill="none" stroke="#1d2a3a" stroke-width="2" stroke-linecap="round" stroke-linejoin="round"/></svg>Better Poop</li>
      <li><svg viewBox="0 0 22 22"><circle cx="11" cy="11" r="9.5" fill="none" stroke="#1d2a3a" stroke-width="1.8"/><polyline points="6.5,11.5 9.7,14.5 15.5,8" fill="none" stroke="#1d2a3a" stroke-width="2" stroke-linecap="round" stroke-linejoin="round"/></svg>Healthy Tummy</li>
      <li class="wide"><svg viewBox="0 0 22 22"><circle cx="11" cy="11" r="9.5" fill="none" stroke="#1d2a3a" stroke-width="1.8"/><polyline points="6.5,11.5 9.7,14.5 15.5,8" fill="none" stroke="#1d2a3a" stroke-width="2" stroke-linecap="round" stroke-linejoin="round"/></svg>Vet Formulated</li>
    </ul>

    <div class="flavor">
      <div class="chew-art" role="img" aria-label="Photo of beef liver flavoured soft chews"></div>
      <p class="flavor-name">Beef Liver<br>Flavor</p>
    </div>
  </section>
</body>
</html>
```